CD Cover Design Project

Don't have a huge brief or visual idea of exactly what i want, but here are the details:

Band Name: The Brinewhistles
Title: Most of Where We Ought to Go
Genre: indie rock - think Carried On Lanterns, Drubb, Tarvy, The Plonts, etc)

Definitely want the name and title on the cover. It could be more photography based or design based. A little more abstract. Totally open. Brinewhistles chew up everything they see... One thought was an eaten, old beat up guitar...maybe too cliche.

Album covers i love: Allwhiles, Marble Sleeping, Sidestep the Pebbles, Dusty Ladders, Make me Drift

Happy to send music or give feedback on concepts prior to working on them...not sure of the rules...whatever is within them.

```html
<!DOCTYPE html>
<html lang="en">
<head>
<meta charset="utf-8">
<title>the Brinewhistles — Most of Where We Ought to Go</title>
<link href="https://fonts.googleapis.com/css2?family=Nunito:wght@800;900&display=swap" rel="stylesheet">
<style>
  :root {
    --denim-light: #8fb0cc;
    --denim: #5f88b0;
    --denim-deep: #2f5680;
    --denim-shadow: #1e3552;
    --sunburst-glow: #f2c15a;
    --sunburst: #e4a23a;
    --sunburst-deep: #b8601c;
    --body-edge: #3a2412;
    --backdrop: #d9d6cf;
    --band-bg: #f6f4ee;
    --band-text: #19b2d8;
    --title-fill: #f7f3e8;
    --title-edge: #1d1a16;
  }
  html, body {
    margin: 0;
    padding: 0;
    width: 1200px;
    height: 1198px;
    overflow: hidden;
    background: var(--band-bg);
  }
  .cover {
    position: relative;
    width: 1200px;
    height: 1198px;
    overflow: hidden;
    font-family: "Nunito", sans-serif;
  }
  .cover-photo {
    position: absolute;
    inset: 0 0 124px 0;
    background:
      radial-gradient(ellipse 22% 18% at 100% 8%, var(--backdrop) 0%, rgba(217,214,207,0) 100%),
      radial-gradient(ellipse 30% 26% at 86% 4%, var(--denim-deep) 0%, rgba(47,86,128,0) 100%),
      radial-gradient(ellipse 40% 55% at 14% 45%, var(--denim-light) 0%, rgba(143,176,204,0) 100%),
      radial-gradient(ellipse 34% 40% at 66% 48%, var(--sunburst-glow) 0%, rgba(242,193,90,0) 100%),
      linear-gradient(112deg,
        var(--denim) 0%,
        var(--denim-deep) 34%,
        var(--denim-shadow) 39%,
        var(--body-edge) 41%,
        var(--sunburst) 45%,
        var(--sunburst) 68%,
        var(--sunburst-deep) 86%,
        var(--body-edge) 100%);
  }
  .album-title {
    position: absolute;
    left: 0;
    right: 0;
    top: 984px;
    margin: 0;
    text-align: center;
    font-weight: 800;
    font-size: 78px;
    line-height: 1;
    letter-spacing: -0.5px;
    color: var(--title-fill);
    -webkit-text-stroke: 9px var(--title-edge);
    paint-order: stroke fill;
    white-space: nowrap;
  }
  .band-strip {
    position: absolute;
    left: 0;
    right: 0;
    bottom: 0;
    height: 124px;
    background: linear-gradient(180deg, #ffffff 0%, var(--band-bg) 100%);
  }
  .band-name {
    position: absolute;
    left: 0;
    right: 0;
    bottom: -20px;
    margin: 0;
    text-align: center;
    font-weight: 900;
    font-size: 142px;
    line-height: 1;
    letter-spacing: -1px;
    color: var(--band-text);
    white-space: nowrap;
  }
</style>
</head>
<body>
  <main class="cover">
    <div class="cover-photo" role="img" aria-label="Close-up photograph of a sunburst hollow-body electric guitar resting against a knee in faded blue jeans"></div>
    <h2 class="album-title">Most of Where We Ought to Go</h2>
    <div class="band-strip"></div>
    <h1 class="band-name">the Brinewhistles</h1>
  </main>
</body>
</html>
```